Updated Stationary needed using new logo for Hair Tissue Mineral Analysis Company

Simple stationary design needed using new logo!
1. 8.5" x 11" Letterhead with company information listed below
2. 8.5" x 11" Design with Footer only with logo and information for print materials
3. 5.5" x 8.5" letterhead design
4. 4.125" x 9.5" Business envelope (#10 envelope) with address
5. 4.125" x 9.5" Business envelope with clear window (#10 envelope) with address
6. 6.5" x 9.5" envelope (6 3/4 Booklet envelope) with address
7. 10" x 13" Open End envelope
Address:
4817 N. Carver Lane
Phoenix, AZ 85021
Phone:
(602)-384-7261
Website:
www.quvenlabs.example
Email:
information@quvenlabs.example
Look and feel
Each slider illustrates characteristics of the customer's brand and the style your logo design should communicate.

```html
<!DOCTYPE html>
<html lang="en">
<head>
<meta charset="utf-8">
<title>Quven Labs Stationery</title>
<link href="https://fonts.googleapis.com/css2?family=Arimo:wght@400;700&display=swap" rel="stylesheet">
<style>
  :root {
    --backdrop: #38393b;
    --paper: #f7f5f5;
    --navy: #1d3c78;
    --orange: #f4862a;
    --ink: #2b2b2b;
    --brand: #2a4a8c;
    --ghost: #e3e7ee;
    --window-edge: #c9c9c9;
  }
  * { box-sizing: border-box; margin: 0; padding: 0; }
  html, body { width: 1200px; height: 442px; overflow: hidden; }
  body {
    background: var(--backdrop);
    position: relative;
    font-family: "Arimo", Arial, sans-serif;
    color: var(--ink);
  }
  .sheet {
    position: absolute;
    background: var(--paper);
    overflow: hidden;
  }
  .corner-swoosh {
    position: absolute;
    top: 0;
    right: 0;
  }
  .brand {
    position: absolute;
    display: flex;
    align-items: center;
    gap: 2px;
    font-weight: 700;
    color: var(--brand);
    font-size: 7px;
    letter-spacing: 0.3px;
    white-space: nowrap;
  }
  .brand-dot {
    width: 5px; height: 5px;
    background: var(--orange);
  }
  .ghost-name {
    position: absolute;
    font-weight: 700;
    color: var(--ghost);
    letter-spacing: 2px;
    line-height: 1;
    white-space: nowrap;
  }
  .contact {
    position: absolute;
    font-size: 4.4px;
    line-height: 5.4px;
    white-space: nowrap;
  }
  .contact .gap { height: 3px; }
  .contact-line { display: flex; align-items: center; gap: 2px; }
  .contact.right { text-align: right; }
  .contact.right .contact-line { justify-content: flex-end; }
  .icon { width: 3.4px; height: 3.4px; display: inline-block; fill: var(--brand); flex: none; }
  .footer-strip {
    position: absolute;
    left: 26px; right: 26px;
    bottom: 6px;
    font-size: 3.9px;
    text-align: center;
    white-space: nowrap;
  }
  .footer-strip .rule { border-top: 0.5px solid #888; margin: 1px 0 3px; }
  .footer-strip .contact-line { justify-content: center; gap: 2px; }
  .address-window {
    position: absolute;
    border: 0.8px solid var(--window-edge);
    border-radius: 3px;
    background: #fbfbfb;
  }
</style>
</head>
<body>
<svg width="0" height="0" style="position:absolute">
  <defs>
    <symbol id="swoosh" viewBox="0 0 100 100" preserveAspectRatio="none">
      <path d="M0,0 H100 V100 C86,46 50,7 0,0 Z" fill="#f4862a"/>
      <path d="M5,0 H100 V88 C94,38 62,2 5,0 Z" fill="#1d3c78"/>
    </symbol>
    <symbol id="i-phone" viewBox="0 0 10 10"><path d="M2 0.5 L4 0.5 L4.6 3 L3.3 3.9 C4 5.6 4.6 6.3 6.1 6.8 L7 5.5 L9.5 6.1 L9.5 8.2 C9.5 9 8.9 9.5 8 9.5 C4 9.3 0.7 6 0.5 2 C0.5 1.1 1 0.5 2 0.5Z"/></symbol>
    <symbol id="i-mail" viewBox="0 0 10 10"><rect x="0.5" y="2" width="9" height="6"/></symbol>
    <symbol id="i-web" viewBox="0 0 10 10"><circle cx="5" cy="5" r="4.5"/></symbol>
  </defs>
</svg>

<!-- Letterhead 8.5 x 11 -->
<section class="sheet" style="left:41px;top:60px;width:255px;height:330px;">
  <svg class="corner-swoosh" style="width:50%;height:34%"><use href="#swoosh"/></svg>
  <div class="brand" style="left:20px;top:27px;"><span class="brand-dot"></span>QUVEN LABS</div>
  <div class="ghost-name" style="left:38px;top:142px;font-size:50px;">QUVEN</div>
  <div class="contact right" style="right:16px;bottom:11px;">
    <div>4817 N. Carver Lane</div>
    <div>Phoenix, AZ 85021</div>
    <div class="gap"></div>
    <div class="contact-line">(602)-384-7261 <svg class="icon"><use href="#i-phone"/></svg></div>
    <div class="contact-line">information@quvenlabs.example <svg class="icon"><use href="#i-mail"/></svg></div>
    <div class="contact-line">www.quvenlabs.example <svg class="icon"><use href="#i-web"/></svg></div>
  </div>
</section>

<!-- Letterhead 5.5 x 8.5 -->
<section class="sheet" style="left:322px;top:136px;width:165px;height:254px;">
  <svg class="corner-swoosh" style="width:65%;height:35%"><use href="#swoosh"/></svg>
  <div class="brand" style="left:14px;top:16px;font-size:6.4px;"><span class="brand-dot"></span>QUVEN LABS</div>
  <div class="ghost-name" style="left:20px;top:108px;font-size:34px;">QUVEN</div>
  <div class="footer-strip">
    <div>4817 N. Carver Lane, Phoenix, AZ 85021</div>
    <div class="rule"></div>
    <div class="contact-line">
      <svg class="icon"><use href="#i-phone"/></svg>(602)-384-7261
      <svg class="icon"><use href="#i-mail"/></svg>information@quvenlabs.example
      <svg class="icon"><use href="#i-web"/></svg>www.quvenlabs.example
    </div>
  </div>
</section>

<!-- Open end envelope 10 x 13 -->
<section class="sheet" style="left:511px;top:20px;width:330px;height:256px;">
  <svg class="corner-swoosh" style="width:40%;height:43%"><use href="#swoosh"/></svg>
  <div class="brand" style="left:16px;top:17px;"><span class="brand-dot"></span>QUVEN LABS</div>
  <div class="contact" style="left:16px;top:34px;">
    <div>4817 N. Carver Lane</div>
    <div>Phoenix, AZ 85021</div>
    <div class="gap"></div>
    <div class="contact-line"><svg class="icon"><use href="#i-phone"/></svg>(602)-384-7261</div>
    <div class="contact-line"><svg class="icon"><use href="#i-mail"/></svg>information@quvenlabs.example</div>
    <div class="contact-line"><svg class="icon"><use href="#i-web"/></svg>www.quvenlabs.example</div>
  </div>
  <div class="ghost-name" style="right:14px;top:192px;font-size:58px;">QUVEN</div>
</section>

<!-- Booklet envelope 6.5 x 9.5 -->
<section class="sheet" style="left:866px;top:83px;width:285px;height:195px;">
  <svg class="corner-swoosh" style="width:46%;height:55%"><use href="#swoosh"/></svg>
  <div class="brand" style="left:15px;top:20px;"><span class="brand-dot"></span>QUVEN LABS</div>
  <div class="contact" style="left:15px;top:37px;">
    <div>4817 N. Carver Lane</div>
    <div>Phoenix, AZ 85021</div>
    <div class="gap"></div>
    <div class="contact-line"><svg class="icon"><use href="#i-phone"/></svg>(602)-384-7261</div>
    <div class="contact-line"><svg class="icon"><use href="#i-mail"/></svg>information@quvenlabs.example</div>
    <div class="contact-line"><svg class="icon"><use href="#i-web"/></svg>www.quvenlabs.example</div>
  </div>
  <div class="ghost-name" style="right:10px;top:145px;font-size:48px;">QUVEN</div>
</section>

<!-- #10 envelope with window -->
<section class="sheet" style="left:534px;top:301px;width:285px;height:124px;">
  <svg class="corner-swoosh" style="width:45%;height:100%"><use href="#swoosh"/></svg>
  <div class="brand" style="left:11px;top:16px;"><span class="brand-dot"></span>QUVEN LABS</div>
  <div class="contact" style="left:11px;top:33px;">
    <div>4817 N. Carver Lane</div>
    <div>Phoenix, AZ 85021</div>
    <div class="gap"></div>
    <div class="contact-line"><svg class="icon"><use href="#i-phone"/></svg>(602)-384-7261</div>
    <div class="contact-line"><svg class="icon"><use href="#i-mail"/></svg>information@quvenlabs.example</div>
    <div class="contact-line"><svg class="icon"><use href="#i-web"/></svg>www.quvenlabs.example</div>
  </div>
  <div class="address-window" style="left:12px;top:74px;width:120px;height:37px;"></div>
  <div class="ghost-name" style="right:6px;top:82px;font-size:36px;">QUVEN</div>
</section>

<!-- #10 business envelope -->
<section class="sheet" style="left:867px;top:301px;width:285px;height:124px;">
  <svg class="corner-swoosh" style="width:45%;height:100%"><use href="#swoosh"/></svg>
  <div class="brand" style="left:17px;top:19px;"><span class="brand-dot"></span>QUVEN LABS</div>
  <div class="contact" style="left:17px;top:36px;">
    <div>4817 N. Carver Lane</div>
    <div>Phoenix, AZ 85021</div>
    <div class="gap"></div>
    <div class="contact-line"><svg class="icon"><use href="#i-phone"/></svg>(602)-384-7261</div>
    <div class="contact-line"><svg class="icon"><use href="#i-mail"/></svg>information@quvenlabs.example</div>
    <div class="contact-line"><svg class="icon"><use href="#i-web"/></svg>www.quvenlabs.example</div>
  </div>
  <div class="ghost-name" style="right:10px;top:72px;font-size:46px;">QUVEN</div>
</section>
</body>
</html>
```